Harbor Sushi & Steak Dinner Menu

I'm looking for a MENU design with a particular feel. I want to have a base template made that I can then use for future alterations to the menu; ie I can go in and change out different entrees as the menu changes but the template will remain the same. (Ideally it would be in an Apple Pages format.). Also ideally - dinner menu will occupy 2 pages 8.5 x 11. The restaurant's name is Harbor. It is a MODERN steak house that will also feature Sushi, a Raw Bar, Exquisite Cocktails and a sophisticated nightlife crowd. I have attached our LOGO, a secondary logo that we will be featuring throughout the project including on the menu cover (the gold U). Finally - I have attached the content that we would like to see. AGAIN - I REITERATE: High end dining and lounge atmosphere. A couple of restaurants / menus that I love are Corvellin in NYC and Marrowby Steakhouse in Long Island NY. Please do not duplicate - just trying to offer some suggestions.

Requirements
Must have
• A sophisticated and elegant feel without being stuffy or old.

```html
<!DOCTYPE html>
<html lang="en">
<head>
<meta charset="utf-8">
<title>Harbor Sushi &amp; Steak — Dinner Menu</title>
<link href="https://fonts.googleapis.com/css2?family=Dosis:wght@500;600;700&family=Open+Sans:wght@400;600&display=swap" rel="stylesheet">
<style>
:root{
  --canvas:#e6e4e5;
  --ink:#0b0b0b;
  --slate:#2b2b2d;
  --slate-deep:#151516;
  --red:#d42c3c;
  --gold:#c9b37a;
  --gold-soft:#e3d5a8;
  --cream:#d9cfb2;
  --rule:#5b5a56;
  --paper:#ffffff;
}
*{box-sizing:border-box;margin:0;padding:0}
html,body{width:1188px;height:1200px;overflow:hidden;background:var(--canvas)}
body{position:relative;font-family:"Open Sans",sans-serif}
.spread{position:absolute;left:204px;width:782px;height:506px;display:flex}
.spread--cover{top:60px}
.spread--inside{top:620px}
.page{position:relative;width:391px;height:506px;overflow:hidden}

/* cover */
.back-cover{background:linear-gradient(90deg,var(--paper) 55%,#ececec 100%)}
.brand-mark{position:absolute;left:0;right:0;top:318px;display:flex;justify-content:center;align-items:center;gap:6px}
.brand-mark__name{font-family:"Dosis",sans-serif;font-weight:600;letter-spacing:4px;font-size:24px;color:var(--gold)}
.brand-mark__dot{width:8px;height:8px;border-radius:50%;background:var(--red)}
.back-cover__url{position:absolute;left:0;right:0;top:451px;text-align:center;font-size:6px;color:var(--red)}
.front-cover{background:var(--ink)}
.front-cover__photo{position:absolute;left:40px;top:0;width:312px;height:268px;
  background:linear-gradient(150deg,#f6f1ea 0%,#f08a4d 35%,#3a3a36 55%,#f29a5e 75%,#b48a5a 100%);
  clip-path:polygon(0 0,100% 0,100% 88%,80% 95%,40% 92%,10% 100%,0 96%)}
.front-cover__frames{position:absolute;inset:0}
.front-cover__logo{position:absolute;left:20px;right:21px;top:372px;display:flex;justify-content:center;align-items:center;gap:8px}
.front-cover__logo .brand-mark__name{font-size:32px;letter-spacing:6px}

/* inside */
.inside{background:linear-gradient(180deg,var(--slate) 0%,#1d1d1f 60%,var(--slate-deep) 100%)}
.inside::before,.inside::after{content:"";position:absolute;left:0;right:0;height:7px;background:linear-gradient(90deg,#4a4334,var(--gold) 40%,#6e6144 100%)}
.inside::before{top:0}
.inside::after{bottom:0}
.food-strip{position:absolute;left:0;top:0;bottom:0;width:90px;z-index:1;
  background:linear-gradient(180deg,#b8502c 0%,#e8a070 22%,#f4ece2 40%,#2a2522 52%,#f09a62 66%,#c0402a 84%,#8a2a1a 100%);
  clip-path:polygon(0 0,100% 0,92% 25%,100% 50%,90% 75%,100% 100%,0 100%)}
.block{position:absolute;z-index:2}
.rule-v{position:absolute;width:1px;background:var(--rule);z-index:2}
.rule-h{position:absolute;height:1px;background:var(--rule);z-index:2}

.heading{position:relative;display:inline-block;isolation:isolate;font-family:"Dosis",sans-serif;font-weight:600;color:var(--gold-soft);font-size:13px;line-height:1.2;margin-bottom:8px}
.heading::before{content:"";position:absolute;left:55%;right:-18px;top:3px;bottom:3px;background:var(--red);z-index:-1}
.heading--sm{font-size:10.5px;margin-bottom:6px}

.item{font-size:8.5px;line-height:1.1;margin-bottom:6px}
.item__name{font-family:"Dosis",sans-serif;font-weight:500;color:var(--red);font-size:8.5px}
.item__desc{display:block;font-size:4.6px;color:var(--cream);line-height:1.3}
.item--inline{margin-bottom:4.6px}
.item--inline .item__desc{display:inline;margin-left:4px}
.item--tight{margin-bottom:3.4px}
.item--gold .item__name{color:#c9a46a}
.item--roomy{margin-bottom:10px}

.banner{position:absolute;left:99px;top:274px;z-index:2;font-family:"Dosis",sans-serif;font-weight:700;color:var(--red);font-size:25px;line-height:1.2;white-space:nowrap}

.side-group{display:flex;gap:8px}
.side-group__label{writing-mode:vertical-rl;transform:rotate(180deg);font-family:"Dosis",sans-serif;font-weight:600;color:var(--red);font-size:11px;letter-spacing:4px;border-left:1px solid var(--rule);padding-left:4px;height:76px;text-align:left}
.side-group ul{list-style:none;font-size:5px;color:var(--cream);line-height:13px}
</style>
</head>
<body>

<section class="spread spread--cover">
  <div class="page back-cover">
    <div class="brand-mark">
      <span class="brand-mark__name">HARBOR</span><span class="brand-mark__dot"></span>
    </div>
    <p class="back-cover__url">www.harbordining.com</p>
  </div>
  <div class="page front-cover">
    <div class="front-cover__photo" role="img" aria-label="Close-up photo of salmon and crab nigiri sushi with black chopsticks"></div>
    <svg class="front-cover__frames" width="391" height="506" viewBox="0 0 391 506" aria-hidden="true">
      <rect x="20.5" y="23.5" width="350" height="459" fill="none" stroke="#c9b37a" stroke-width="1.5"/>
      <polyline points="67,24 67,262 0,262" fill="none" stroke="#c9b37a" stroke-width="1.5"/>
      <polyline points="343,140 391,140" fill="none" stroke="#c9b37a" stroke-width="1.5"/>
    </svg>
    <div class="front-cover__logo">
      <span class="brand-mark__name">HARBOR</span><span class="brand-mark__dot"></span>
    </div>
  </div>
</section>

<section class="spread spread--inside">
  <div class="page inside">
    <div class="food-strip" role="img" aria-label="Photo strip of shrimp, sushi rolls with chopsticks and red lobster"></div>
    <div class="rule-v" style="left:234px;top:30px;height:234px"></div>
    <div class="rule-v" style="left:234px;top:318px;height:168px"></div>

    <div class="block" style="left:98px;top:26px;width:128px">
      <h2 class="heading">SUSHI | SASHIMI</h2>
      <div class="item item--inline"><span class="item__name">Toro</span><span class="item__desc">blue fin tuna belly (gf)</span></div>
      <div class="item item--inline"><span class="item__name">Ebi</span><span class="item__desc">cooked shrimp (gf)</span></div>
      <div class="item item--inline"><span class="item__name">Hamachi</span><span class="item__desc">yellowtail (gf)</span></div>
      <div class="item item--inline"><span class="item__name">Uni</span><span class="item__desc">sea urchin (gf)</span></div>
      <div class="item item--inline"><span class="item__name">Hirame</span><span class="item__desc">fluke (gf)</span></div>
      <div class="item item--inline"><span class="item__name">Unagi</span><span class="item__desc">fresh water eel (gf)</span></div>
      <div class="item item--inline"><span class="item__name">Sake</span><span class="item__desc">salmon (gf)</span></div>
      <div class="item item--inline"><span class="item__name">Madai</span><span class="item__desc">red snapper (gf)</span></div>
      <div class="item item--inline"><span class="item__name">Maguro</span><span class="item__desc">tuna (gf)</span></div>
    </div>
    <div class="rule-h" style="left:98px;width:126px;top:184px"></div>
    <div class="block" style="left:99px;top:192px;width:128px">
      <h2 class="heading heading--sm">SUSHI PLATTERS</h2>
      <div class="item item--inline item--roomy"><span class="item__name">Small:</span><span class="item__desc">Five pieces assorted sushi, nine pieces sashimi, spicy tuna roll (gf)</span></div>
      <div class="item item--inline"><span class="item__name">Large:</span><span class="item__desc">Eight pieces assorted sushi, eighteen pieces sashimi, alaska roll, rainbow roll (gf)</span></div>
    </div>

    <div class="block" style="left:248px;top:26px;width:132px">
      <h2 class="heading">SPECIAL ROLLS</h2>
      <div class="item"><span class="item__name">The Harbor</span><span class="item__desc">tuna, salmon, yellowtail, avocado, spicy mayo, soy bean paper</span></div>
      <div class="item"><span class="item__name">King Crab Rainbow</span><span class="item__desc">king crab, avocado, cucumbers, assorted fish on top</span></div>
      <div class="item"><span class="item__name">Empress</span><span class="item__desc">shrimp tempura, spicy tuna on top, eel sauce, spicy mayo</span></div>
      <div class="item"><span class="item__name">Spicy Girl</span><span class="item__desc">spicy crunchy crab meat, cucumber, shrimp on top</span></div>
      <div class="item"><span class="item__name">Dragon</span><span class="item__desc">eel, cucumber, avocado, and tobiko on top, eel sauce</span></div>
      <div class="item"><span class="item__name">Yummy</span><span class="item__desc">spicy crunchy salmon, avocado, mango and salmon on top</span></div>
      <div class="item"><span class="item__name">No. 9</span><span class="item__desc">shrimp tempura, avocado, kani, spicy mayo, tobiko</span></div>
      <div class="item"><span class="item__name">Sunrise Roll</span><span class="item__desc">spicy crunchy tuna and avocado, spicy crunchy salmon on top</span></div>
    </div>

    <div class="rule-h" style="left:98px;width:282px;top:268px"></div>
    <p class="banner">SUSHI . STEAK . COCKTAILS</p>

    <div class="block" style="left:99px;top:316px;width:128px">
      <h2 class="heading heading--sm">SEA FOOD RAW BAR</h2>
      <div class="item item--tight"><span class="item__name">Lobster Cocktail</span></div>
      <div class="item item--tight"><span class="item__name">Shrimp Cocktail</span></div>
      <div class="item item--tight"><span class="item__name">Clams on the Half Shell</span></div>
      <div class="item item--tight"><span class="item__name">Oysters on the Half Shell</span></div>
      <div class="item item--tight"><span class="item__name">Colossal Crab Cocktail</span></div>
    </div>
    <div class="rule-h" style="left:98px;width:126px;top:402px"></div>
    <div class="block" style="left:99px;top:408px;width:128px">
      <div class="item item--roomy"><span class="item__name">Raw Bar Plate for One</span><span class="item__desc">Two Shrimp, Half of a One Pound Lobster, Two Clams, One East Coast Oyster, One West Coast Oyster</span></div>
      <div class="item"><span class="item__name">Seafood Platters (gf):</span><span class="item__desc">Shrimp, Oysters, Clams, Lobster &amp; Crab<br>Large or Colossal</span></div>
    </div>

    <div class="block" style="left:248px;top:316px;width:136px">
      <h2 class="heading">CLASSIC ROLLS</h2>
      <div class="item item--tight"><span class="item__name">Yellowtail</span><span class="item__desc">inside out roll with scallions (gf)</span></div>
      <div class="item item--tight"><span class="item__name">Spicy Tuna or Salmon or Yellowtail</span><span class="item__desc">spicy mayo</span></div>
      <div class="item item--tight"><span class="item__name">California</span><span class="item__desc">crab meat, cucumber and avocado (gf)</span></div>
      <div class="item item--tight"><span class="item__name">Vegetable</span><span class="item__desc">avocado, cucumber, asparagus and pickled reddish (gf)</span></div>
      <div class="item item--tight"><span class="item__name">Spider</span><span class="item__desc">soft shell crab and avocado with eel sauce</span></div>
      <div class="item item--tight"><span class="item__name">Shrimp Tempura</span><span class="item__desc">deep fried tempura shrimp and eel sauce</span></div>
      <div class="item item--tight"><span class="item__name">Alaskan</span><span class="item__desc">salmon and avocado (gf)</span></div>
    </div>
  </div>

  <div class="page inside">
    <div class="food-strip" style="width:86px" role="img" aria-label="Photo strip of shrimp, sushi rolls with chopsticks and red lobster"></div>
    <div class="rule-v" style="left:233px;top:34px;height:362px"></div>

    <div class="block" style="left:99px;top:30px;width:124px">
      <h2 class="heading">ENTREES</h2>
      <div class="item"><span class="item__name">Pan Roasted Miso Glazed<br>Black Cod</span><span class="item__desc">green tea noodle stir fry, napa cabbage, carrot, japanese eggplant</span></div>
      <div class="item"><span class="item__name">Pan Seared Striped Bass</span><span class="item__desc">lobster succotash in a tomato saffron broth</span></div>
      <div class="item"><span class="item__name">E.V.O.O. Slated /<br>Grilled Swordfish</span><span class="item__desc">sun dried tomato, olive and caper tapenade over basmati rice</span></div>
      <div class="item"><span class="item__name">Grilled Half Chicken</span><span class="item__desc">sun dried tomato and basil israeli cous-cous, pan au jus</span></div>
      <div class="item"><span class="item__name">Roasted Fresh Cavatelle<br>Ratatoille</span><span class="item__desc">vegetable broth</span></div>
      <div class="item"><span class="item__name">Lobster Cartoccio</span><span class="item__desc">shrimp, mussels, clams, fresh herb tomato broth, tossed with bucatini</span></div>
      <div class="item"><span class="item__name">Charred Artichoke Hearts</span><span class="item__desc">heirloom tomatoes, caper berries, spring onions, fresh basil, white wine reduction over forbidden rice (gf)</span></div>
      <div class="item"><span class="item__name">Mediterranean Grilled Veggie Plate</span><span class="item__desc">artichoke hearts, japanese eggplant, green &amp; white asparagus, seared heirloom tomatoes, roasted baby carrots, cauliflower rice, evoo &amp; fig drizzle (gf)</span></div>
    </div>
    <div class="rule-h" style="left:98px;width:126px;top:311px"></div>
    <div class="block" style="left:99px;top:318px;width:124px">
      <h2 class="heading heading--sm">USDA PRIME STEAKS</h2>
      <div class="item item--gold item--tight"><span class="item__name">10 Oz Filet</span></div>
      <div class="item item--gold item--tight"><span class="item__name">14 or 16 oz New York Strip</span></div>
      <div class="item item--gold item--tight"><span class="item__name">24 oz Boneless Ribeye</span></div>
      <div class="item item--gold item--tight"><span class="item__name">36 oz Bone In Ribeye</span></div>
      <div class="item item--gold item--tight"><span class="item__name">Berkshire Pork chop</span></div>
    </div>

    <div class="block" style="left:247px;top:30px;width:130px">
      <h2 class="heading">APPS</h2>
      <div class="item"><span class="item__name">BAO Bun</span><span class="item__desc">hoisin bbq pancetta cut pork loin, crispy onions, micro mint</span></div>
      <div class="item"><span class="item__name">Five Spice Crispy Popcorn Crusted Prawns (2)</span><span class="item__desc">classic burre blanc</span></div>
      <div class="item"><span class="item__name">Jumbo Lump Crab</span><span class="item__desc">citrus miso drizzle, spring pea puree, micro greens</span></div>
      <div class="item"><span class="item__name">Crispy Wonton Napoleon</span><span class="item__desc">cucumber gallete, ahi tuna, jumbo lump crab meat, wasabi aioli, shoestring wontons</span></div>
      <div class="item"><span class="item__name">PEI Mussels</span><span class="item__desc">charred artichoke hearts, blistered heirloom tomatoes, garlic white wine broth</span></div>
      <div class="item"><span class="item__name">New Zealand or Domestic Small Eye Lamb Chop (1)</span><span class="item__desc">crispy porcini risotto cake</span></div>
    </div>
    <div class="rule-h" style="left:247px;width:124px;top:220px"></div>
    <div class="block" style="left:247px;top:226px;width:130px">
      <h2 class="heading">SALAD</h2>
      <div class="item item--tight"><span class="item__name">Classic Wedge</span><span class="item__desc">bleu cheese, bacon lardons, heirloom tomatoes</span></div>
      <div class="item item--tight"><span class="item__name">Mixed Baby Greens</span><span class="item__desc">heirloom tomatoes, cucumber, red onion, dijon vinaigrette</span></div>
      <div class="item item--tight"><span class="item__name">Tabulleh</span><span class="item__desc">buckwheat grain, fresh mint, tomato concasse, cucumber, parsley, fresh squeezed lemon, EVOO, salt and pepper</span></div>
      <div class="item item--tight"><span class="item__name">Tomato Mozzarella Salad/Burratta</span></div>
      <div class="item item--tight"><span class="item__name">Spinach Salad</span><span class="item__desc">green apple, feta, currants, with persimmons vinaigrette</span></div>
      <div class="item item--tight"><span class="item__name">Kale Caesar</span><span class="item__desc">homemade cacio e' peppe dressing, pecorino and parmesan chees, toasted croutons</span></div>
    </div>

    <div class="rule-h" style="left:93px;width:276px;top:404px"></div>
    <div class="block side-group" style="left:102px;top:412px">
      <span class="side-group__label">SAUCES</span>
      <ul><li>Cabernet Demi Glaz</li><li>Gorganzola Brulle Cream</li><li>Truffled Wild Mushroom Ragu</li><li>Horseradish Cream</li><li>House Steak Sauce</li></ul>
    </div>
    <div class="block side-group" style="left:203px;top:412px;gap:10px">
      <span class="side-group__label">SIDES</span>
      <ul style="line-height:12px"><li>Mashed Idaho Potatoes</li><li>Roasted Peanut Potatoes</li><li>Creamed Spinach</li><li>Sauteed Spinach</li><li>Bacon, Sweet corn,</li><li>Caramelized Vidalia</li></ul>
      <ul style="line-height:11.5px"><li>Onion Fingerling potatoes</li><li>Grilled Asparagus</li><li>French Beans</li><li>Israeli Cous Cous</li><li>Sweet Potato Steak Fries</li><li>Corn Skillet</li></ul>
    </div>
  </div>
</section>

</body>
</html>
```